Dr Delwyn's Letterhead

I need a professional neat letterhead incorporating my professional information, university titles and qualifications. I have attached my 3 recent ones which contain all the necessary information that needs to be included. I am happy for the information to be a side bar left or right, or as a header/footer combination.

Hello all

I have now made a 2nd and 3rd prize so please submit

Reason: Now there is a 2nd and 3rd place so I can take 3 designs

University

```html
<!DOCTYPE html>
<html lang="en">
<head>
<meta charset="utf-8">
<title>Dr Anselm Delwyn – Letterhead</title>
<link rel="stylesheet" href="https://fonts.googleapis.com/css2?family=Noto+Sans:wght@400&display=swap">
<style>
  :root {
    --backdrop: #47484d;
    --paper: #ffffff;
    --brand-blue: #1c4b93;
    --ink: #1a1a1a;
    --rule: #222222;
    --crest-red: #8e2430;
    --crest-gold: #e2b437;
  }
  * { margin: 0; padding: 0; box-sizing: border-box; }
  html, body {
    width: 1200px; height: 935px; overflow: hidden;
    background: var(--backdrop);
    font-family: "Noto Sans", "DejaVu Sans", sans-serif;
    color: var(--ink);
  }
  .letterhead {
    position: absolute;
    left: 289px; top: 27px;
    width: 622px; height: 880px;
    background: var(--paper);
    box-shadow: 0 10px 30px rgba(0,0,0,.35);
  }
  .band { position: absolute; left: 0; right: 0; height: 11px; background: var(--brand-blue); }
  .band--top { top: 0; }
  .band--bottom { bottom: 0; }

  .practitioner {
    position: absolute; left: 26px; top: 98px;
    line-height: 1;
  }
  .practitioner__name {
    font-size: 31px; font-weight: 400; letter-spacing: .3px;
    margin-bottom: 6px;
  }
  .practitioner__details { list-style: none; font-size: 9.6px; line-height: 11.6px; }

  .rooms {
    position: absolute; right: 26px; top: 24px;
    list-style: none; text-align: right;
    font-size: 9.2px; line-height: 11.4px;
  }
  .header-rule {
    position: absolute; left: 60px; right: 26px; top: 205px;
    border: 0; border-top: 1px solid var(--rule);
  }

  .affiliations {
    position: absolute; right: 26px; bottom: 22px;
    text-align: right; font-size: 9.4px; line-height: 11.6px;
  }
  .badges {
    position: absolute; left: 26px; bottom: 20px;
    display: flex; gap: 8px; align-items: flex-end;
  }
</style>
</head>
<body>
  <main class="letterhead">
    <div class="band band--top"></div>

    <header>
      <ul class="rooms">
        <li>28/90 larkspur road</li>
        <li>specialist medical centre</li>
        <li>harbourside nsw 2190</li>
        <li>14 ferris highway</li>
        <li>ferris specialist centre</li>
        <li>millbrook nsw 2172</li>
        <li>p 95550142 95550187</li>
        <li>f 95550163</li>
      </ul>

      <div class="practitioner">
        <h1 class="practitioner__name">dr. anselm delwyn</h1>
        <ul class="practitioner__details">
          <li>BSc (Med) MBBS (Hons 1) EVU FRACS (Oto)</li>
          <li>adult and paediatric ENT</li>
          <li>head and neck surgery</li>
          <li>consultant &amp; senior lecturer</li>
          <li>harbourside hospital and area health service</li>
          <li>university of kellerton</li>
        </ul>
      </div>
      <hr class="header-rule">
    </header>

    <footer>
      <div class="badges">
        <svg class="badge" width="26" height="30" viewBox="0 0 26 30" role="img" aria-label="Affiliated university badge">
          <path d="M1 1h24v14c0 8-6 12-12 14C7 27 1 23 1 15z" fill="var(--crest-red)"/>
        </svg>
        <svg class="badge" width="30" height="32" viewBox="0 0 30 32" role="img" aria-label="Affiliated college badge">
          <circle cx="15" cy="16" r="14" fill="var(--crest-gold)"/>
        </svg>
      </div>
      <p class="affiliations">
        the harbourside public and private<br>
        hospitals/northgate private hospital<br>
        prov no 4812376K
      </p>
    </footer>

    <div class="band band--bottom"></div>
  </main>
</body>
</html>
```